Natural Dog Treat Box Label

We're looking for a modern, eye-catching label for our Natural Dog Treat Box. The design should clearly communicate the contents of the box, appealing to customers and highlighting the natural, wholesome ingredients inside

Brand Name: Merry Paws
Label Size: 210 mm x 148 mm Landscape
EAN Barcode: 5031847260591

Merry Paws Natural Treat Box for Dogs

Treat your dog to the ultimate natural snack experience with our Merry Paws Natural Treat Box. Packed with a variety of high-quality, single-ingredient chews, this box is designed to satisfy your dog's instincts while promoting dental health and overall well-being. Each treat is carefully sourced and free from artificial additives, offering your pet a wholesome and delicious indulgence.

Contents:
Chicken Feet (100g): A natural source of protein and collagen to support joint health.
Duck Feet (100g): Rich in nutrients and perfect for strong teeth and gums.
Beef Trachea (100g): Great for satisfying chewing while helping to clean teeth and promote healthy digestion.
Pork Bites (100g): Tasty, protein-packed bites your dog will love.
Chicken Necks (100g): A crunchy, flavorful treat that’s high in calcium and great for teeth cleaning.
Rabbit Ears (100g): A lean, hypoallergenic treat that’s gentle on sensitive stomachs.
Pig Ears (x2): A long-lasting chew that helps keep your dog entertained and satisfied.
Ideal for dogs of all sizes, the Merry Paws Natural Treat Box offers a variety of textures and flavors to keep your dog engaged and happy. Whether you're looking to reward your dog, support their health, or just give them a tasty treat, this box has something they'll love!

Preferably Natural Colours

Target Market(s)

Dog Owners

Industry/Entity Type

Pet Supplies

Requirements
Nice to have
• Product Contents Icons

```html
<!DOCTYPE html>
<html lang="en">
<head>
<meta charset="utf-8">
<title>Merry Paws Natural Treat Box Label</title>
<link rel="stylesheet" href="https://fonts.googleapis.com/css2?family=Anton&family=Fira+Sans:ital,wght@1,800&family=Poppins:wght@400;600&display=swap">
<style>
  :root {
    --sky: #5ecbef;
    --sky-deep: #2f9dcb;
    --blue-title: #22a3cf;
    --orange: #f26722;
    --paper: #f0f0f2;
    --ink: #3d3d3f;
    --teal: #17a3a8;
    --white: #ffffff;
    --backdrop: #d8d8d8;
    --c1: #5bc8ef; --c2: #f7941d; --c3: #ec1c5b; --c4: #128478;
    --c5: #4e2a7d; --c6: #8dc63f; --c7: #c1272d;
  }
  * { margin: 0; padding: 0; box-sizing: border-box; }
  html, body { width: 845px; height: 1200px; overflow: hidden; background: var(--backdrop); }
  .label {
    position: absolute; left: 0; top: 302px; width: 845px; height: 596px;
    background: var(--paper); overflow: hidden; font-family: "Poppins", sans-serif;
  }
  .sky-band { position: absolute; left: 0; top: 0; width: 100%; height: 215px;
    background: linear-gradient(180deg, var(--sky), var(--sky-deep)); }
  .orange-band { position: absolute; left: 0; top: 215px; width: 100%; height: 34px; background: var(--orange); }
  .brand-mark { position: absolute; left: 62px; top: 23px; width: 120px; text-align: center; }
  .brand-mark .square { display: block; width: 81px; height: 80px; margin: 0 0 0 19px; background: var(--white); border-radius: 3px; }
  .brand-mark .name { display: block; margin-top: 6px; font-family: "Anton", sans-serif; font-size: 38px; line-height: 42px; color: var(--white); letter-spacing: 1px; }
  .badge { position: absolute; left: 246px; top: 18px; width: 350px; height: 350px; border-radius: 50%;
    background: var(--paper); border: 6px solid var(--teal); box-shadow: inset 0 0 0 7px var(--sky); text-align: center; }
  .badge .maker { margin-top: 70px; font-family: "Fira Sans", sans-serif; font-style: italic; font-weight: 800; font-size: 36px; line-height: 40px; }
  .badge .maker .warm { color: var(--orange); }
  .badge .maker .cool { color: var(--ink); }
  .badge .headline { font-family: "Anton", sans-serif; color: var(--blue-title); font-size: 80px; line-height: 78px; letter-spacing: 1px; }
  .badge .sub { font-family: "Fira Sans", sans-serif; font-style: italic; font-weight: 800; font-size: 28px; color: var(--ink); margin-top: 2px; }
  .dog-photo { position: absolute; left: 552px; top: 30px; width: 293px; height: 420px; }
  .intro { position: absolute; left: 27px; top: 258px; width: 390px; }
  .intro h2 { font-family: "Fira Sans", sans-serif; font-style: italic; font-weight: 800; font-size: 16.5px; line-height: 20px; color: var(--blue-title); }
  .intro p { margin-top: 3px; font-size: 13.6px; line-height: 18.4px; color: var(--ink); }
  .tagline { position: absolute; left: 0; top: 417px; width: 617px; height: 31px; background: var(--blue-title);
    font-family: "Fira Sans", sans-serif; font-style: italic; font-weight: 800; font-size: 17px; line-height: 31px; color: var(--white); padding-left: 29px; }
  .contents { position: absolute; left: 0; top: 448px; width: 845px; height: 107px; }
  .contents svg { position: absolute; left: 0; top: 0; }
  .item { position: absolute; top: 10px; width: 108px; color: var(--white); font-size: 10.6px; line-height: 12.6px; }
  .item .icon { display: block; width: 20px; height: 20px; border-radius: 50%; border: 2.5px solid var(--white); margin-bottom: 11px; }
  .item b { display: block; font-family: "Fira Sans", sans-serif; font-style: italic; font-weight: 800; font-size: 10.6px; }
  .footer { position: absolute; left: 0; top: 555px; width: 100%; height: 41px; background: var(--orange); color: var(--white); }
  .footer .weight { position: absolute; left: 29px; top: 8px; font-size: 18px; }
  .footer .ean { position: absolute; right: 25px; top: 7px; font-size: 19px; font-weight: 600; letter-spacing: 0.5px; }
</style>
</head>
<body>
<main class="label">
  <div class="sky-band"></div>
  <div class="orange-band"></div>

  <div class="brand-mark">
    <span class="square"></span>
    <span class="name">MERRY<br>PAWS</span>
  </div>

  <section class="intro">
    <h2>Wholesome Treats<br>for a Healthier, Happier Dog!</h2>
    <p>Treat your dog to the ultimate<br>natural snack experience! Packed<br>with high-quality, single-ingredient<br>chews, this box promotes dental<br>health and overall well-being. Wholesome, delicious,<br>and free from artificial additives.</p>
  </section>

  <div class="badge">
    <div class="maker"><span class="warm">Merry</span> <span class="cool">Paws</span></div>
    <div class="headline">NATURAL<br>TREAT</div>
    <div class="sub">Box for Dogs</div>
  </div>

  <svg class="dog-photo" viewBox="0 0 293 420" role="img" aria-label="Photo of a smiling golden retriever sitting">
    <defs>
      <linearGradient id="fur" x1="0" y1="0" x2="0" y2="1">
        <stop offset="0" stop-color="#d99a4e"/>
        <stop offset="0.6" stop-color="#e0ad6c"/>
        <stop offset="1" stop-color="#f2dcc0"/>
      </linearGradient>
    </defs>
    <path d="M30 80 Q40 10 120 5 Q200 2 230 60 Q245 120 260 160 Q293 200 293 260 L293 420 L40 420 Q20 320 40 240 Q10 180 30 80 Z" fill="url(#fur)"/>
  </svg>

  <div class="tagline">Wholesome, natural, and healthy indulgence.</div>

  <section class="contents">
    <svg width="845" height="107" viewBox="0 0 845 107" aria-hidden="true">
      <polygon points="0,0 120,0 143,53 120,107 0,107" fill="var(--c1)"/>
      <polygon points="120,0 235,0 258,53 235,107 120,107 143,53" fill="var(--c2)"/>
      <polygon points="235,0 350,0 373,53 350,107 235,107 258,53" fill="var(--c3)"/>
      <polygon points="350,0 465,0 488,53 465,107 350,107 373,53" fill="var(--c4)"/>
      <polygon points="465,0 580,0 603,53 580,107 465,107 488,53" fill="var(--c5)"/>
      <polygon points="580,0 695,0 718,53 695,107 580,107 603,53" fill="var(--c6)"/>
      <polygon points="695,0 845,0 845,107 695,107 718,53" fill="var(--c7)"/>
    </svg>
    <div class="item" style="left:27px"><span class="icon"></span><b>Chicken Feet (100g)</b>Protein and<br>collagen for<br>joint health.</div>
    <div class="item" style="left:153px"><span class="icon"></span><b>Duck Feet (100g)</b>Nutrients for<br>strong teeth<br>and gums.</div>
    <div class="item" style="left:262px"><span class="icon"></span><b>Beef Trachea (100g)</b>Cleans teeth<br>and aids<br>digestion.</div>
    <div class="item" style="left:380px"><span class="icon"></span><b>Pork Bites (100g)</b>Tasty,<br>protein-packe<br>d bites.</div>
    <div class="item" style="left:493px"><span class="icon"></span><b>Chicken Necks<br>(100g)</b>Crunchy treats<br>high in calcium.</div>
    <div class="item" style="left:607px"><span class="icon"></span><b>Rabbit Ears (100g)</b>Lean,<br>hypoallergenic<br>treat for sensitive<br>stomachs.</div>
    <div class="item" style="left:724px;width:115px"><span class="icon"></span><b>Pig Ears (x2)</b>Long-lasting<br>chew to keep your<br>dog entertained.</div>
  </section>

  <footer class="footer">
    <span class="weight">NET WEIGHT 5.0 OZ</span>
    <span class="ean">5031847260591</span>
  </footer>
</main>
</body>
</html>
```